Vodka label for New Brand called KIRO Vodka

We need a label measuring 3.5 inches wide & 5 inches tall for this vodka bottle. The brand is "KIRO Vodka". This should be the largest font on the label. "Handcrafted in the USA" should be on bottle in small font near the bottom. The tagline "Keeping It Real Onward" also needs to be included anywhere that makes sense in a smaller font than the brand name. Also in smaller font at the bottom/corners- "80 proof, 750 ml, 40% alc/vol" I value the human mind over AI, but am providing a couple designs that were AI generated to give you a better idea where to start and what we are looking for. Thank you!

Target Market(s)

21-45 year olds.

Industry/Entity Type

Alcohol

Colors
0054AA
0677BA
7BADD7
CADEEF
E8F1F8
EB3D1F
EC4F4E
F09395
F8D3D4
FCEDEE

Requirements
Should not have
• You can not use the US flag but can use elements of it.

```html
<!DOCTYPE html>
<html lang="en">
<head>
<meta charset="utf-8">
<title>KIRO Vodka Label</title>
<link href="https://fonts.googleapis.com/css2?family=Alfa+Slab+One&family=Montserrat:wght@800&family=Oswald:wght@500;600&display=swap" rel="stylesheet">
<style>
  :root {
    --navy: #1c3166;
    --red: #b51d3d;
    --white: #ffffff;
    --backdrop: #ececec;
  }
  html, body {
    margin: 0;
    width: 1200px;
    height: 960px;
    overflow: hidden;
    background: var(--backdrop);
  }
  .stage {
    width: 1200px;
    height: 960px;
    display: flex;
    align-items: center;
    justify-content: center;
  }
  .label { width: 620px; height: 760px; display: block; }
  .brand-name { font-family: "Alfa Slab One", serif; font-size: 178px; fill: var(--white); letter-spacing: 4px; }
  .tagline { font-family: "Montserrat", sans-serif; font-weight: 800; font-size: 17px; letter-spacing: 4px; fill: var(--white); }
  .product-type { font-family: "Oswald", sans-serif; font-weight: 600; font-size: 54px; letter-spacing: 9px; fill: var(--navy); }
  .origin { font-family: "Oswald", sans-serif; font-weight: 600; font-size: 29px; letter-spacing: 0.5px; fill: var(--navy); }
  .specs { font-family: "Oswald", sans-serif; font-weight: 500; font-size: 18px; letter-spacing: 0.5px; fill: var(--navy); white-space: pre; }
  .star-large { fill: var(--white); }
  .star-small { fill: var(--navy); }
</style>
</head>
<body>
<main class="stage">
  <svg class="label" viewBox="0 0 620 760" role="group" aria-label="KIRO Vodka bottle label">
    <defs>
      <path id="star" d="M0,-10 L2.35,-3.24 9.51,-3.09 3.8,1.24 5.88,8.09 0,4 -5.88,8.09 -3.8,1.24 -9.51,-3.09 -2.35,-3.24 Z"/>
      <path id="tagline-arc" d="M70,405 Q310,330 560,330"/>
    </defs>

    <g class="stripes">
      <rect x="0" y="430" width="620" height="260" fill="var(--white)"/>
      <g fill="var(--red)">
        <rect x="10" y="430" width="24" height="260"/>
        <rect x="58" y="430" width="24" height="260"/>
        <rect x="106" y="430" width="24" height="260"/>
        <rect x="154" y="430" width="24" height="260"/>
        <rect x="202" y="430" width="24" height="260"/>
        <rect x="250" y="430" width="24" height="260"/>
        <rect x="298" y="430" width="24" height="260"/>
        <rect x="346" y="430" width="24" height="260"/>
        <rect x="394" y="430" width="24" height="260"/>
        <rect x="442" y="430" width="24" height="260"/>
        <rect x="490" y="430" width="24" height="260"/>
        <rect x="538" y="430" width="24" height="260"/>
        <rect x="586" y="430" width="24" height="260"/>
      </g>
    </g>

    <path class="crest" d="M0,190 L300,40 L620,70 L620,420 L0,420 Z" fill="var(--navy)"/>
    <path class="crest-edge" d="M0,190 L300,40 L620,70" fill="none" stroke="var(--red)" stroke-width="8"/>
    <rect class="crest-base" x="0" y="420" width="620" height="10" fill="var(--red)"/>

    <g class="crest-stars">
      <use href="#star" class="star-large" transform="translate(240,125) scale(1.5)"/>
      <use href="#star" class="star-large" transform="translate(310,100) scale(2.6)"/>
      <use href="#star" class="star-large" transform="translate(380,120) scale(1.5)"/>
    </g>

    <text class="brand-name" x="310" y="322" text-anchor="middle">KIRO</text>

    <text class="tagline"><textPath href="#tagline-arc" startOffset="50%" text-anchor="middle">KEEPING IT REAL ONWARD</textPath></text>

    <path class="product-panel" d="M200,382 H420 V465 Q310 505 200 465 Z" fill="var(--white)"/>
    <text class="product-type" x="314" y="455" text-anchor="middle">VODKA</text>

    <rect class="base-band" x="0" y="690" width="620" height="70" fill="var(--navy)"/>

    <g class="info-panel">
      <rect x="80" y="628" width="460" height="114" fill="var(--white)" stroke="var(--navy)" stroke-width="6"/>
      <rect x="94" y="640" width="432" height="90" fill="none" stroke="var(--navy)" stroke-width="1.5"/>
      <text class="origin" x="310" y="682" text-anchor="middle">HANDCRAFTED IN THE USA</text>
      <text class="specs" x="310" y="713" text-anchor="middle">80 PROOF   |   40% ALC/VOL   |   750 ML</text>
      <use href="#star" class="star-small" transform="translate(112,661) scale(0.7)"/>
      <use href="#star" class="star-small" transform="translate(112,685) scale(0.7)"/>
      <use href="#star" class="star-small" transform="translate(112,709) scale(0.7)"/>
      <use href="#star" class="star-small" transform="translate(508,661) scale(0.7)"/>
      <use href="#star" class="star-small" transform="translate(508,685) scale(0.7)"/>
      <use href="#star" class="star-small" transform="translate(508,709) scale(0.7)"/>
    </g>
  </svg>
</main>
</body>
</html>
```